Brand Identity Pack - Communications Services Company

We require our brand identity to be developed further and something we can move across additional brands we are launching. At the moment we have a mixed message around what our businesses brand is and want to concrete this and improve it. We have one element which is like the business card attached and the other which is on our website.

we have a new slogan we want to reiterate across our branding which is;

Consult>Connect>Care

we want to implement this into our logo and website.

areas we want to cover are;

business Cards
Logo update (if you feel the slogan should go in)
Comp slips
Letterhead
A4 Folder
Facebook (look at current)
Twitter (look at current)

We also have a Vantor glide we want to put our brand identity on.

www.brenwickcomms.co.uk is our website.

we are launching Brenwick Payment Services (Card Payment Terminals) of which we have the logo designed and intend to use the same consult>connect>Care as our slogan. This needs to go within our branding.

I have loaded a business card with some of our branding which is slightly confusing and not in line.

help us make our brand super strong :)

Regards
Joss

Industry/Entity Type

It Company

```html
<!DOCTYPE html>
<html lang="en">
<head>
<meta charset="utf-8">
<title>Brenwick Payment Services – Business Card</title>
<link href="https://fonts.googleapis.com/css2?family=Arimo:wght@400;700&display=swap" rel="stylesheet">
<style>
  :root {
    --backdrop: #9c7a55;
    --card-white: #ffffff;
    --ink: #111111;
    --brand-blue: #1b9ad7;
    --brand-blue-light: #3aa8de;
    --on-dark: #ffffff;
  }
  * { box-sizing: border-box; margin: 0; padding: 0; }
  html, body {
    width: 1071px;
    height: 1200px;
    overflow: hidden;
  }
  body {
    background: var(--backdrop);
    font-family: "Arimo", Arial, sans-serif;
    position: relative;
  }
  .card {
    position: absolute;
    width: 880px;
    height: 497px;
    border-radius: 34px;
    overflow: hidden;
  }
  .card--front { left: 87px; top: 42px; background: var(--card-white); }
  .card--back  { left: 92px; top: 580px; background: var(--brand-blue); }

  .front-waves { position: absolute; inset: 0; }

  .brand {
    position: absolute;
    left: 150px;
    top: 96px;
    width: 520px;
    text-align: center;
  }
  .brand__name {
    font-weight: 700;
    font-size: 82px;
    line-height: 1;
    letter-spacing: 1px;
    color: var(--ink);
  }
  .brand__tagline {
    margin-top: 20px;
    font-weight: 400;
    font-size: 32px;
    letter-spacing: 3px;
    color: var(--brand-blue-light);
  }

  .holder {
    position: absolute;
    left: 38px;
    top: 398px;
    color: var(--on-dark);
  }
  .holder__name { font-weight: 700; font-size: 29px; }
  .holder__role { font-size: 20px; margin-top: 8px; }

  .contacts {
    position: absolute;
    right: 35px;
    top: 318px;
    list-style: none;
    color: var(--on-dark);
    font-size: 21px;
    text-align: right;
  }
  .contacts li {
    display: flex;
    justify-content: flex-end;
    align-items: center;
    gap: 8px;
    height: 33.5px;
  }
  .contacts svg { width: 18px; height: 18px; fill: var(--on-dark); }

  .back-brand {
    position: absolute;
    left: 0; right: 0;
    top: 185px;
    text-align: center;
    font-weight: 700;
    font-size: 112px;
    line-height: 1;
    letter-spacing: 2px;
    color: var(--on-dark);
  }
  .slogan {
    position: absolute;
    left: 0; right: 0;
    top: 420px;
    display: flex;
    justify-content: center;
    align-items: center;
    gap: 10px;
    font-weight: 700;
    font-size: 31px;
    color: var(--on-dark);
  }
  .slogan__dot {
    width: 16px; height: 16px;
    border-radius: 50%;
    background: var(--on-dark);
  }
</style>
</head>
<body>

<section class="card card--front">
  <svg class="front-waves" viewBox="0 0 880 497" preserveAspectRatio="none" aria-hidden="true">
    <path d="M0 185 C120 250 230 360 360 358 C520 355 680 250 880 245 L880 497 L0 497 Z" fill="#111111"/>
    <path d="M0 200 C120 270 230 345 360 340 C520 333 680 262 880 262" fill="none" stroke="#1b9ad7" stroke-width="9"/>
    <path d="M0 178 C120 240 240 320 380 318 C540 315 690 252 880 240" fill="none" stroke="#111111" stroke-width="3"/>
  </svg>

  <div class="brand">
    <div class="brand__name">BRENWICK</div>
    <div class="brand__tagline">payment services</div>
  </div>

  <div class="holder">
    <div class="holder__name">Joss Dalby</div>
    <div class="holder__role">Managing Director</div>
  </div>

  <ul class="contacts">
    <li>
      <svg viewBox="0 0 18 18"><rect x="5" y="1" width="8" height="16" rx="1.5"/><rect x="6.5" y="3" width="5" height="7" fill="#111"/></svg>
      07700 900 418
    </li>
    <li>
      <svg viewBox="0 0 18 18"><path d="M4 1 L7 1 L8 5 L6 7 C7 10 8 11 11 12 L13 10 L17 11 L17 14 C17 16 15 17 13 17 C7 16 2 11 1 5 C1 3 2 1 4 1 Z"/></svg>
      01632 960 214
    </li>
    <li>
      <svg viewBox="0 0 18 18"><rect x="1" y="7" width="16" height="8" rx="1.5"/><rect x="4" y="2" width="10" height="6"/><rect x="4" y="10" width="10" height="2" fill="#111"/></svg>
      01632 960 215
    </li>
    <li>
      <svg viewBox="0 0 18 18"><rect x="1" y="4" width="16" height="11" rx="1"/><path d="M1 4 L9 11 L17 4" fill="none" stroke="#111" stroke-width="1.5"/></svg>
      joss@brenwickcomms.co.uk
    </li>
    <li>
      <svg viewBox="0 0 18 18"><circle cx="9" cy="9" r="8"/><path d="M1 9 H17 M9 1 C5 5 5 13 9 17 M9 1 C13 5 13 13 9 17" fill="none" stroke="#111" stroke-width="1.2"/></svg>
      www.brenwickcomms.co.uk
    </li>
  </ul>
</section>

<section class="card card--back">
  <div class="back-brand">BRENWICK</div>
  <div class="slogan">
    <span class="slogan__dot"></span>
    <span>ADVISE • LINK • SUPPORT</span>
  </div>
</section>

</body>
</html>
```